quote template for plumbing serivce for homeowners

Design Brief – Plumbing Quotation Document
1. Brand & Style
• Business: Plumbing (Maintenance focus, premium service)
• Positioning: Professional, trustworthy, high-end, compliant, reliable
• Tone: Clean, modern, premium trades, easy to read, confidence-building
• Colours: Use brand colours (or leave placeholders: Primary / Secondary / Accent)
• Fonts:
o Headings: Bold, clean, modern (e.g. Montserrat, Poppins, Inter)
o Body text: Simple and highly readable (e.g. Inter, Lato, Open Sans)
• Layout Feel: Structured, not cluttered, strong hierarchy, visually balanced, logical flow
• Imagery: Minimal – allow subtle plumbing or technical icons, but do not overpower text
2. Document Requirements
✅ Must Include:
Cover Page
• Logo
• Business name
• Tagline (if applicable)
• Document title: Quotation / Proposal
• Client name, site address, quote number, date
• Business contact details (phone, email, website, licence number optional)
• Optional photo banner or design strip (clean and minimal)
Section 1 – Introduction
• Short professional message thanking them, setting expectations
• Optional small “Our promise” or “What to expect” note
Section 2 – Price Options
• Must support unlimited quote sections / options (Option 1, Option 2, Option 3 etc.)
• Each option should include:
o Detailed description
o Price
o Optional tick/check icons to highlight benefits
• Layout must allow adding or removing options easily without breaking format
• Pricing to be emphasised but not overpower the description
Section 3 – Total Investment
• Clearly display:
o Subtotal
o GST
o Total
• Include optional line for:
o Deposit (if applicable)
o Payment terms (optional)
• Should stand out using contrast box or section highlight
Section 4 – Why Choose Us
Include space or icons for key trust points. Must allow content similar to:
• Licensed & insured plumbing professionals
• Lifetime labour warranty on workmanship
• Premium materials and compliant installations
• Transparent pricing, no hidden surprises
• On-time, tidy, and customer-focused
• Australian Standards compliant (AS/NZS 3500)
• Local, trusted, reviewed business
Designer to create layout that supports 5–8 trust points using icons or bold highlights.
Section 5 – Terms & Conditions
Must allow a text area for:
• Quote validity
• What is/what isn’t included
• Warranty notes
• Site access requirements
• Variations clause
• Payment terms
Section 6 – Acceptance
Needs to include:
• Signature line
• Print name
• Date
• Option to tick selected option if multiple options provided
• “Approval to proceed” section
Optional Page Elements
(Include if space allows)
• Certifications or licence numbers
• Quorvix review rating or testimonial section
• Before/after photo box (if relevant)
• QR code linking to website or booking page
• Small footer with company details on each page
3. Functional Requirements
• Must be:
o Easy to edit (headings, prices, options, text blocks)
o Expandable (sections must duplicate without breaking layout)
o Saveable as PDF
o Professional when printed
o Visually aligned to premium home & commercial clients
• Page numbering required (Page 1 of X)
• Consistent header or footer with business name/logo
4. Deliverables Needed
Designer to supply:
1. Master editable template (Canva, Word, or InDesign INDD)
2. PDF export version
3. Style guide (fonts, sizes, colours)
4. Instructions for duplicating option sections easily
5. Design Inspiration Keywords
• Premium trade proposal
• Clean modern layout
• Structured price options
• Trust-building visuals
• Technical but customer-friendly
• Compliant and confident
home owners
plumbing

```html
<!DOCTYPE html>
<html lang="en">
<head>
<meta charset="utf-8">
<title>Harbourline Plumbing – Quotation Template Pages</title>
<link rel="stylesheet" href="https://fonts.googleapis.com/css2?family=Poppins:wght@400;500;600;700;800&display=swap">
<style>
:root{
  --bg:#d3cfd0;
  --paper:#ffffff;
  --blue:#0b4fa6;
  --cyan:#2bb6e2;
  --yellow:#f8bb1b;
  --ink:#2c2c2c;
  --soft:#eceef1;
  --line:#e9d79a;
}
*{margin:0;padding:0;box-sizing:border-box}
html,body{width:1200px;height:796px;overflow:hidden;background:var(--bg);font-family:'Poppins',sans-serif;color:var(--ink)}
.board{position:relative;width:1200px;height:796px}
.page{position:absolute;width:254px;height:329px;background:var(--paper);overflow:hidden}
.page > *{position:absolute}
.running-head{left:20px;top:18px;width:214px;display:flex;align-items:center;gap:4px;font-size:6.6px;font-weight:600;color:var(--blue)}
.running-head::after{content:"";flex:1;height:0.6px;background:var(--line)}
.section-title{left:20px;font-size:10.8px;font-weight:600;color:var(--blue)}
.body-copy{font-size:4.3px;line-height:6.7px;text-align:justify;color:#333}
.page-foot{left:20px;top:297px;width:214px;display:flex;align-items:center;gap:5px}
.foot-brand{font-size:5px;font-weight:700;color:var(--blue);line-height:5.4px;width:30px}
.foot-rule{flex:1;height:0.6px;background:var(--cyan)}
.foot-num{font-size:6.4px;font-weight:600;color:var(--cyan)}
.photo{border-radius:3px}

/* cover */
.cover-brand{left:0;width:254px;top:22px;text-align:center;font-size:17px;font-weight:800;color:var(--blue);line-height:19px;letter-spacing:0.5px}
.cover-photo{left:64px;top:79px;width:124px;height:124px;border-radius:50%;background:conic-gradient(#c9a93a 0 25%,#1d6fb9 0 50%,#c8a13a 0 75%,#1a5aa3 0);border:2px solid #fff}
.cover-name{left:0;width:254px;top:212px;text-align:center;font-size:16.5px;font-weight:800;color:var(--blue);letter-spacing:0.3px}
.cover-tagline{left:69px;top:235px;width:111px;height:12px;border-radius:6px;background:var(--yellow);color:var(--blue);font-size:7px;text-align:center;line-height:12px}
.cover-field{font-size:4.1px;font-weight:600;color:var(--blue)}
.cover-band{left:0;top:304px;width:254px;height:25px;background:var(--cyan);display:flex;align-items:center;padding:0 10px 0 20px;gap:5px}
.contact-item{font-size:3.9px;color:#fff;line-height:5px;padding-right:5px;border-right:0.5px solid #fff}
.contact-item:last-child{border-right:0}

/* promise */
.step{width:48px;text-align:center}
.step-num{font-size:11px;font-weight:700;line-height:11px}
.step-dial{width:40px;height:20px;border-radius:20px 20px 0 0;margin:3px auto 0;position:relative}
.step-icon{position:absolute;left:8px;top:5px;width:24px;height:24px;border-radius:50%;background:#fff;box-shadow:0 1px 3px rgba(0,0,0,.2);display:flex;align-items:center;justify-content:center}
.step-card{width:48px;height:52px;background:#eef0f3;margin-top:10px;padding-top:10px;clip-path:polygon(0 14%,50% 0,100% 14%,100% 100%,0 100%)}
.step-card b{display:block;font-size:5px;font-weight:600;color:#222}
.step-card p{font-size:4.6px;line-height:6.4px;color:#333;padding:1px 3px 0}
.step-bar{height:3px;margin-top:1px}
.dash{left:20px;top:165px;width:214px;border-top:0.7px dashed #b9bec6}

/* price options */
.option{left:20px;width:214px;height:65px;background:var(--blue);border-radius:3px;color:#fff;padding:4px 11px 0 16px}
.option-head{display:flex;justify-content:space-between;font-size:8.3px;font-weight:700;padding-bottom:3px;border-bottom:0.6px solid rgba(255,255,255,.7);margin:0 -11px 0 0;padding-right:11px}
.option p{font-size:4.4px;line-height:6.3px;margin-top:4px;text-align:justify}
.option ul{font-size:4.4px;line-height:7.3px;margin-top:1px;padding-left:6px}

/* investment */
.field-box{width:111px;height:17px;border:0.8px solid var(--blue);border-radius:1px;padding:2px 5px;font-size:5.3px;font-weight:700;color:var(--blue);line-height:5.6px}
.invest-table{left:20px;top:106px;width:214px;border-collapse:collapse;table-layout:fixed}
.invest-table th{height:26px;font-size:5.7px;font-weight:700;color:#fff;border:0.6px solid #fff;line-height:6px}
.invest-table th small{display:block;font-weight:400;font-size:5.6px}
.invest-table td{height:15.2px;border:0.6px solid var(--cyan)}
.invest-table .total{background:var(--yellow);color:var(--blue);font-size:7px;font-weight:700;text-align:center}

/* why choose us */
.trust{left:20px;width:214px;height:24px;background:var(--soft);display:flex;align-items:center}
.trust-icon{width:19px;height:19px;border-radius:50%;margin-left:-1px;display:flex;align-items:center;justify-content:center;box-shadow:0 0 0 2px #fff}
.trust span{font-size:6.1px;margin-left:9px;color:#222}

/* terms */
.term-pill{left:20px;width:214px;height:7.5px;border-radius:4px;background:var(--yellow);font-size:4.2px;font-weight:600;padding-left:6px;line-height:7.5px;color:#222}
.term-copy{left:20px;width:214px;font-size:3.4px;line-height:5px;color:#333}
.payment-box{left:20px;top:238px;width:214px;height:54px;background:var(--blue);border-radius:3px;color:#fff;padding:6px 6px}
.payment-box h4{font-size:6px;font-weight:500}
.payment-box ul{font-size:3.6px;line-height:6.5px;margin-top:3px;padding-left:12px}

/* acceptance */
.check-row{left:21px;width:213px;display:flex;gap:6px;font-size:4.4px;line-height:6.4px}
.check-row i{flex:0 0 7px;height:7px;border:0.6px solid #333;border-radius:1px;margin-top:1px}
.sign-label{font-size:4.6px;font-weight:700;color:#111}
</style>
</head>
<body>
<main class="board">

  <section class="page cover" style="left:54px;top:50px">
    <div class="cover-brand">HARBOURLINE<br>PLUMBING</div>
    <div class="cover-photo" role="img" aria-label="Circular photo collage: plumber in overalls holding a wrench, framed by plumbing work scenes in yellow and blue tints"></div>
    <h1 class="cover-name">BUSINESS NAME</h1>
    <div class="cover-tagline">Tagline Will be added Here</div>
    <div class="cover-field" style="left:20px;top:271px">Quotation / Proposal :</div>
    <div class="cover-field" style="left:20px;top:279px">Client Name :</div>
    <div class="cover-field" style="left:20px;top:287px">Site Address :</div>
    <div class="cover-field" style="left:149px;top:271px">Quote Number :</div>
    <div class="cover-field" style="left:149px;top:279px">Date :</div>
    <div class="cover-band">
      <div class="contact-item">Phone Number :<br>000-000-0000</div>
      <div class="contact-item">Email :<br>companyname@mailbox.com</div>
      <div class="contact-item">Website :<br>www.companyname.com</div>
      <div class="contact-item">Licence Number :<br>0000000000000</div>
    </div>
  </section>

  <section class="page" style="left:331px;top:50px">
    <div class="running-head">Business Name</div>
    <h2 class="section-title" style="top:37px">1. Introduction</h2>
    <p class="body-copy" style="left:20px;top:63px;width:214px">Lorem Ipsum is simply dummy text of the printing and typesetting industry. Lorem Ipsum has been the industry's standard dummy text ever since the 1500s, when an unknown printer took a galley of type and scrambled it to make a type specimen book. It has survived not only five centuries, but also the leap into electronic typesetting, remaining essentially unchanged.</p>
    <p class="body-copy" style="left:20px;top:104px;width:214px">It was popularised in the 1960s with the release of transfer sheets containing Lorem Ipsum passages, and more recently with desktop layout software including many versions of Lorem Ipsum.</p>
    <h3 style="left:20px;top:137px;font-size:5.6px;font-weight:600">Lorem Ipsum is simply dummy text</h3>
    <p class="body-copy" style="left:20px;top:147px;width:111px">Lorem Ipsum is simply dummy text of the printing and typesetting industry. Lorem Ipsum has been the industry's standard dummy text ever since the 1500s, when an unknown printer took a galley of type and scrambled it to make a type specimen book. It has survived not only five centuries, but also the leap into electronic typesetting, remaining essentially unchanged. It was popularised in the 1960s with the release of transfer sheets containing Lorem Ipsum passages.</p>
    <div style="left:152px;top:139px;width:83px;height:97px;background:var(--yellow);border-radius:4px"></div>
    <div class="photo" role="img" aria-label="Photo of a plumber kneeling to repair pipes under a kitchen sink" style="left:148px;top:135px;width:83px;height:96px;background:linear-gradient(135deg,#c9b8a2,#7d6a58 55%,#3d4a66)"></div>
    <p class="body-copy" style="left:20px;top:248px;width:214px">It was popularised in the 1960s with the release of transfer sheets containing Lorem Ipsum passages, and more recently with desktop layout software including many versions of Lorem Ipsum.</p>
    <footer class="page-foot"><span class="foot-brand">HARBOURLINE PLUMBING</span><span class="foot-rule"></span><span class="foot-num">02</span></footer>
  </section>

  <section class="page" style="left:608px;top:50px">
    <div class="running-head">Business Name</div>
    <h2 class="section-title" style="top:39px">Our Promise</h2>
    <p class="body-copy" style="left:20px;top:61px;width:214px">Lorem Ipsum is simply dummy text of the printing and typesetting industry. Lorem Ipsum has been the industry's standard dummy text ever since the 1500s, when an unknown printer took a galley of type and scrambled it to make a type specimen book. It has survived not only five centuries, but also the leap into electronic typesetting, remaining essentially unchanged.</p>
    <div class="dash"></div>
    <div class="step" style="left:29px;top:109px">
      <div class="step-num" style="color:var(--yellow)">01</div>
      <div class="step-dial" style="background:var(--yellow)"><div class="step-icon"><svg width="11" height="11" viewBox="0 0 12 12"><circle cx="6" cy="6" r="5" fill="none" stroke="#333" stroke-width="0.9"/><path d="M6 3v3l2 1.3" fill="none" stroke="#333" stroke-width="0.9"/></svg></div></div>
      <div class="step-card"><b>Lorem 1</b><p>Lorem Ipsum is simply dummy text of the printing.</p></div>
      <div class="step-bar" style="background:var(--yellow)"></div>
    </div>
    <div class="step" style="left:99px;top:109px">
      <div class="step-num" style="color:var(--blue)">02</div>
      <div class="step-dial" style="background:var(--blue)"><div class="step-icon"><svg width="11" height="11" viewBox="0 0 12 12"><path d="M6 11C2 8 2 4 6 1c4 3 4 7 0 10zM6 11V5" fill="none" stroke="#333" stroke-width="0.9"/></svg></div></div>
      <div class="step-card"><b>Lorem 2</b><p>Lorem Ipsum is simply dummy text of the printing.</p></div>
      <div class="step-bar" style="background:var(--blue)"></div>
    </div>
    <div class="step" style="left:170px;top:109px">
      <div class="step-num" style="color:var(--cyan)">03</div>
      <div class="step-dial" style="background:var(--cyan)"><div class="step-icon"><svg width="11" height="11" viewBox="0 0 12 12"><path d="M2 10h8c0-3-2-4-4-3L5 2H3l1 5-2 3z" fill="none" stroke="#333" stroke-width="0.9"/></svg></div></div>
      <div class="step-card"><b>Lorem 3</b><p>Lorem Ipsum is simply dummy text of the printing.</p></div>
      <div class="step-bar" style="background:var(--cyan)"></div>
    </div>
    <div class="photo" role="img" aria-label="Photo of hands fitting a grey irrigation pipe with a red valve among green plants" style="left:20px;top:234px;width:214px;height:54px;background:linear-gradient(90deg,#3d4a3a,#7a8d6a 40%,#5e8f3b 70%,#9cc466)"></div>
    <footer class="page-foot"><span class="foot-brand">HARBOURLINE PLUMBING</span><span class="foot-rule"></span><span class="foot-num">03</span></footer>
  </section>

  <section class="page" style="left:885px;top:50px">
    <div class="running-head">Business Name</div>
    <h2 class="section-title" style="top:36px">2. Price Options</h2>
    <article class="option" style="top:66px">
      <div class="option-head"><span>OPTION 1</span><span>$2,000</span></div>
      <p>Lorem Ipsum is simply dummy text of the printing and typesetting industry. Lorem Ipsum has been the industry's .</p>
      <ul><li>Lorem Ipsum is simply dummy text of the printing and typesetting</li><li>Lorem Ipsum is simply dummy text of the</li><li>Dummy text of the printing and typesetting</li></ul>
    </article>
    <article class="option" style="top:139px">
      <div class="option-head"><span>OPTION 2</span><span>$5,000</span></div>
      <p>Lorem Ipsum is simply dummy text of the printing and typesetting industry. Lorem Ipsum has been the industry's .</p>
      <ul><li>Lorem Ipsum is simply dummy text of the printing and typesetting</li><li>Lorem Ipsum is simply dummy text of the</li><li>Dummy text of the printing and typesetting</li></ul>
    </article>
    <article class="option" style="top:213px">
      <div class="option-head"><span>OPTION 3</span><span>$8,000</span></div>
      <p>Lorem Ipsum is simply dummy text of the printing and typesetting industry. Lorem Ipsum has been the industry's .</p>
      <ul><li>Lorem Ipsum is simply dummy text of the printing and typesetting</li><li>Lorem Ipsum is simply dummy text of the</li><li>Dummy text of the printing and typesetting</li></ul>
    </article>
    <footer class="page-foot"><span class="foot-brand">HARBOURLINE PLUMBING</span><span class="foot-rule"></span><span class="foot-num">04</span></footer>
  </section>

  <section class="page" style="left:54px;top:418px">
    <div class="running-head">Business Name</div>
    <h2 class="section-title" style="top:36px">3. Total Investment</h2>
    <div class="field-box" style="left:20px;top:62px">Investment<br>Account:</div>
    <div class="field-box" style="left:137px;top:62px;width:97px">Initial<br>Investment:</div>
    <div class="field-box" style="left:20px;top:83px">Investor<br>Name:</div>
    <div class="field-box" style="left:137px;top:83px;width:97px">Date of<br>Investment:</div>
    <table class="invest-table">
      <colgroup><col style="width:39px"><col style="width:37px"><col style="width:80px"><col style="width:58px"></colgroup>
      <tr><th style="background:var(--blue)">Subtotal</th><th style="background:var(--blue)">GST</th><th style="background:var(--cyan)">Deposit<small>(if applicable)</small></th><th style="background:var(--cyan)">Payment terms<small>(optional)</small></th></tr>
      <tr><td></td><td></td><td></td><td></td></tr>
      <tr><td></td><td></td><td></td><td></td></tr>
      <tr><td></td><td></td><td></td><td></td></tr>
      <tr><td></td><td></td><td></td><td></td></tr>
      <tr><td></td><td></td><td></td><td></td></tr>
      <tr><td></td><td></td><td></td><td></td></tr>
      <tr><td></td><td></td><td></td><td></td></tr>
      <tr><td></td><td></td><td></td><td></td></tr>
      <tr><td colspan="2" class="total">Total</td><td></td><td></td></tr>
      <tr><td></td><td></td><td></td><td></td></tr>
    </table>
    <footer class="page-foot"><span class="foot-brand">HARBOURLINE PLUMBING</span><span class="foot-rule"></span><span class="foot-num">05</span></footer>
  </section>

  <section class="page" style="left:331px;top:418px">
    <div class="running-head">Business Name</div>
    <h2 class="section-title" style="top:38px">4. Why Choose Us</h2>
    <div class="trust" style="top:68px"><div class="trust-icon" style="background:var(--yellow)"><svg width="9" height="9" viewBox="0 0 10 10"><rect x="2" y="1" width="6" height="8" fill="none" stroke="#333" stroke-width="0.8"/><path d="M3.5 4h3M3.5 6h3" stroke="#333" stroke-width="0.7"/></svg></div><span>Licensed &amp; insured plumbing professionals</span></div>
    <div class="trust" style="top:105px"><div class="trust-icon" style="background:var(--cyan)"><svg width="9" height="9" viewBox="0 0 10 10"><path d="M5 1l3.5 1.3V5c0 2-1.5 3.3-3.5 4C3 8.3 1.5 7 1.5 5V2.3z" fill="none" stroke="#333" stroke-width="0.8"/><path d="M3.5 5l1 1 2-2" fill="none" stroke="#333" stroke-width="0.8"/></svg></div><span>Life time labour warranty on workmanship</span></div>
    <div class="trust" style="top:145px"><div class="trust-icon" style="background:var(--cyan)"><svg width="9" height="9" viewBox="0 0 10 10"><path d="M2 9V4h4v2h2" fill="none" stroke="#333" stroke-width="0.9"/><path d="M4 4V1" stroke="#333" stroke-width="0.9"/></svg></div><span>Premium materials and compliant installations</span></div>
    <div class="trust" style="top:184px"><div class="trust-icon" style="background:var(--yellow)"><svg width="9" height="9" viewBox="0 0 10 10"><circle cx="5" cy="6" r="3" fill="none" stroke="#333" stroke-width="0.8"/><path d="M5 1v2M4 2l1-1 1 1" fill="none" stroke="#333" stroke-width="0.8"/></svg></div><span>Transparent pricing, no hidden surprises</span></div>
    <div class="trust" style="top:221px"><div class="trust-icon" style="background:var(--cyan)"><svg width="9" height="9" viewBox="0 0 10 10"><circle cx="3" cy="3" r="1.2" fill="#333"/><circle cx="7" cy="3" r="1.2" fill="#333"/><path d="M1 8c1-2 3-2 4-1 1-1 3-1 4 1" fill="none" stroke="#333" stroke-width="0.8"/></svg></div><span>On-time, tidy, and customer-focused</span></div>
    <div class="trust" style="top:260px"><div class="trust-icon" style="background:var(--cyan)"><svg width="9" height="9" viewBox="0 0 10 10"><path d="M5 9S1.5 5.5 1.5 3.5a3.5 3.5 0 0 1 7 0C8.5 5.5 5 9 5 9z" fill="none" stroke="#333" stroke-width="0.8"/><circle cx="5" cy="3.5" r="1.1" fill="#333"/></svg></div><span>Local, trusted, reviewed business</span></div>
    <footer class="page-foot"><span class="foot-brand">HARBOURLINE PLUMBING</span><span class="foot-rule"></span><span class="foot-num">06</span></footer>
  </section>

  <section class="page" style="left:608px;top:418px">
    <div class="running-head">Business Name</div>
    <h2 class="section-title" style="top:35px">5. Terms &amp; Conditions</h2>
    <div class="term-pill" style="top:58px">Quote validity</div>
    <p class="term-copy" style="top:70px">Lorem Ipsum is simply dummy text of the printing and typesetting industry. Lorem Ipsum has been the industry's standard dummy text ever since the 1500s, when an unknown printer took a galley of type and scrambled it to make a type specimen book.</p>
    <div class="term-pill" style="top:94px">What is/what isn't included</div>
    <p class="term-copy" style="top:106px">Lorem Ipsum is simply dummy text of the printing and typesetting industry. Lorem Ipsum has been the industry's standard dummy text ever since the 1500s, when an unknown printer took a galley of type and scrambled it to make a type specimen book. It has survived not only five centuries, but also .</p>
    <div class="term-pill" style="top:133px">Warranty notes</div>
    <p class="term-copy" style="top:145px">Lorem Ipsum is simply dummy text of the printing and typesetting industry. Lorem Ipsum has been the industry's standard dummy text ever since the 1500s, when an unknown printer took a galley of type and scrambled it to make a type specimen book. It has survived not only five centuries, but also .</p>
    <div class="term-pill" style="top:171px">Site access requirements</div>
    <p class="term-copy" style="top:183px">Lorem Ipsum is simply dummy text of the printing and typesetting industry. Lorem Ipsum has been the industry's standard dummy text ever since the 1500s, when an unknown printer took a galley of type and scrambled it to make a type specimen book. It has survived not only five centuries, but also .</p>
    <div class="term-pill" style="top:204px">Variations clause</div>
    <p class="term-copy" style="top:216px">Lorem Ipsum is simply dummy text of the printing and typesetting industry. Lorem Ipsum has been the industry's standard dummy text ever since the 1500s, when an unknown printer took a galley of type and scrambled it to make a type specimen book. It has survived not only five centuries, but also .</p>
    <div class="payment-box">
      <h4>Payment terms</h4>
      <ul><li>Lorem Ipsum is simply dummy text of the printing and typesetting industry.</li><li>Lorem Ipsum is simply dummy text of the printing and typesetting industry</li><li>Lorem Ipsum is simply dummy text of the printing and typesetting industry</li><li>Lorem Ipsum is simply dummy text of the printing and typesetting industry</li></ul>
    </div>
    <footer class="page-foot"><span class="foot-brand">HARBOURLINE PLUMBING</span><span class="foot-rule"></span><span class="foot-num">07</span></footer>
  </section>

  <section class="page" style="left:885px;top:418px">
    <div class="running-head">Business Name</div>
    <h2 class="section-title" style="top:31px">6.&nbsp; Acceptance</h2>
    <p class="body-copy" style="left:20px;top:51px;width:214px">Lorem Ipsum is simply dummy text of the printing and typesetting industry. Lorem Ipsum has been the industry's standard dummy text ever since the 1500s, when an unknown printer took a galley of type and scrambled it to make a type specimen book. It has survived not only five centuries, but also the leap into electronic typesetting, remaining essentially unchanged.</p>
    <div class="check-row" style="top:97px"><i></i><span>Lorem Ipsum is simply dummy text of the printing and typesetting industry. Lorem Ipsum has been the industry's standard</span></div>
    <div class="check-row" style="top:116px"><i></i><span>Lorem Ipsum is simply dummy text of the printing and typesetting industry. Lorem Ipsum has been the industry's standard</span></div>
    <div class="check-row" style="top:135px"><i></i><span>Lorem Ipsum is simply dummy text of the printing and typesetting industry. Lorem Ipsum has been the industry's standard</span></div>
    <div class="check-row" style="top:154px"><i></i><span>Lorem Ipsum is simply dummy text of the printing and typesetting industry. Lorem Ipsum has been the industry's standard</span></div>
    <div class="check-row" style="top:173px"><i></i><span>Lorem Ipsum is simply dummy text of the printing and typesetting industry. Lorem Ipsum has been the industry's standard</span></div>
    <p class="body-copy" style="left:20px;top:192px;width:214px">Lorem Ipsum is simply dummy text of the printing and typesetting industry. Lorem Ipsum has been the industry's standard dummy text ever since the 1500s, when an unknown printer took a galley of type and scrambled .</p>
    <div class="sign-label" style="left:20px;top:233px">Print Name :</div>
    <div class="sign-label" style="left:20px;top:243px">Date :</div>
    <div class="sign-label" style="left:186px;top:232px">Lorem Ipsum</div>
    <div role="img" aria-label="Handwritten signature area" style="left:184px;top:242px;width:38px;height:13px;border-bottom:0.6px solid #555"></div>
    <footer class="page-foot"><span class="foot-brand">HARBOURLINE PLUMBING</span><span class="foot-rule"></span><span class="foot-num">08</span></footer>
  </section>

</main>
</body>
</html>
```